【 概要 】 電子書籍(lumora)の表紙デザインを募集します。 【 依頼内容 】 ・サイズ: 高さ2,560ピクセル、幅1,600ピクセル 10000ピクセル以内(JPEG) ・Lumoraブックス・ステーションの表紙画像の要件を満たすように作成をお願いします。 https://books.lumora-press.example/ja_JP/help/topic/Q734912058 ・参考デザイン:『静寂の育て方』 ※帯を付けないので、上下間の文字配置は若干、下寄りにお願い致します。 ・サブタイトル:退屈癖から離れるための穏やかな挨拶のしかた ・メインタイトル:微笑のツバサ(大) ~「明日へ」と歩む~(小) ・著者名:森岡しんご ・著者名アルファベット:Shingo Morioka ・ターゲット層:30〜50代の社会人 デザイン案を楽しみにお待ちしております。 どうぞよろしくお願いします。 |
適切な質疑応答と、迅速なご対応をいただけたこと。
今後の依頼にも期待ができると考えたこと。
今回が初めての依頼だったこともあり、依頼内容が
言葉足らずだったと反省しております。
多数のご提案をいただき、誠にありがとうございました。

```html
<!DOCTYPE html>
<html lang="ja">
<head>
<meta charset="utf-8">
<title>微笑のツバサ ~「明日へ」と歩む~</title>
<link rel="stylesheet" href="https://fonts.googleapis.com/css2?family=Noto+Sans+JP:wght@300;400;500;700&display=swap">
<style>
  :root {
    --bg-top: #0b0b12;
    --bg-mid: #111322;
    --bg-deep: #07070d;
    --glow-blue: #3a4fb8;
    --glow-violet: #5a3f9a;
    --glow-cyan: #7fa6ff;
    --text-main: #f2f2f6;
    --text-soft: #d7d8e2;
  }
  * { margin: 0; padding: 0; box-sizing: border-box; }
  html, body {
    width: 749px;
    height: 1200px;
    overflow: hidden;
    background: var(--bg-deep);
  }
  .cover {
    position: relative;
    width: 749px;
    height: 1200px;
    overflow: hidden;
    font-family: "Noto Sans JP", sans-serif;
    color: var(--text-main);
    background:
      repeating-linear-gradient(90deg, rgba(255,255,255,0.018) 0 2px, transparent 2px 23px),
      linear-gradient(180deg, var(--bg-top) 0%, var(--bg-mid) 45%, var(--bg-deep) 100%);
  }
  .light-field {
    position: absolute;
    left: 0;
    top: 660px;
    width: 749px;
    height: 540px;
  }
  .title-block {
    position: absolute;
    top: 212px;
    left: 0;
    width: 100%;
    text-align: center;
  }
  .main-title {
    font-weight: 300;
    font-size: 60px;
    letter-spacing: 4px;
    line-height: 1;
  }
  .sub-title {
    margin-top: 30px;
    font-weight: 300;
    font-size: 34px;
    letter-spacing: 2px;
    color: var(--text-soft);
  }
  .tagline {
    position: absolute;
    top: 565px;
    right: 112px;
    display: flex;
    flex-direction: row-reverse;
    gap: 36px;
    align-items: flex-start;
  }
  .tagline-col {
    writing-mode: vertical-rl;
    font-weight: 500;
    font-size: 40px;
    line-height: 1;
    letter-spacing: 2px;
  }
  .tagline-col .accent {
    font-weight: 700;
    font-size: 58px;
    letter-spacing: 4px;
  }
  .tagline-col.offset { margin-top: 92px; }
  .author {
    position: absolute;
    top: 1060px;
    left: 0;
    width: 100%;
    text-align: center;
    padding-left: 20px;
  }
  .author-name {
    font-weight: 400;
    font-size: 30px;
    letter-spacing: 3px;
  }
  .author-roman {
    margin-top: 4px;
    font-weight: 400;
    font-size: 17px;
    letter-spacing: 1px;
    color: var(--text-soft);
  }
</style>
</head>
<body>
<main class="cover">
  <svg class="light-field" role="img" aria-label="青紫の光の粒と光の筋が下から立ち上る抽象的な背景" viewBox="0 0 749 540" preserveAspectRatio="none">
    <defs>
      <linearGradient id="fieldFade" x1="0" y1="0" x2="0" y2="1">
        <stop offset="0" stop-color="#1a1f4a" stop-opacity="0"/>
        <stop offset="0.45" stop-color="#2b3585" stop-opacity="0.55"/>
        <stop offset="1" stop-color="#120f2a" stop-opacity="0.9"/>
      </linearGradient>
      <radialGradient id="fieldGlow" cx="0.5" cy="0.65" r="0.6">
        <stop offset="0" stop-color="#6d86ff" stop-opacity="0.45"/>
        <stop offset="0.5" stop-color="#5a3f9a" stop-opacity="0.25"/>
        <stop offset="1" stop-color="#07070d" stop-opacity="0"/>
      </radialGradient>
    </defs>
    <rect width="749" height="540" fill="url(#fieldFade)"/>
    <rect width="749" height="540" fill="url(#fieldGlow)"/>
  </svg>

  <header class="title-block">
    <h1 class="main-title">微笑のツバサ</h1>
    <p class="sub-title">~「明日へ」と歩む~</p>
  </header>

  <section class="tagline" aria-label="退屈癖から離れるための穏やかな挨拶のしかた">
    <p class="tagline-col"><span class="accent">退屈癖</span>から</p>
    <p class="tagline-col">離れるための</p>
    <p class="tagline-col offset">穏やかな</p>
    <p class="tagline-col offset"><span class="accent">挨拶</span>のしかた</p>
  </section>

  <footer class="author">
    <p class="author-name">森岡しんご</p>
    <p class="author-roman">Shingo Morioka</p>
  </footer>
</main>
</body>
</html>
```